Store Fixture business needs a buisness card design

We are looking for a business card design for a store fixture company. "KL Shelf Outfitters" we help small businesses with their start up by providing fixtures required to display their products.
It should have a simple yet innovative design in the front, and a refined look to our company.
We would like our logo, to have one of our products "display cases, clothing rack, mannequins" integrated in the design. And the rest of it just a clean look, which gives our address, store hours, and contact number, etc.
The color scheme as seen in the samples can be changed as long as the goal is achieved.
Industry/Entity Type
Business
Contact Information for Business Card
KL Shelf Outfitters
4362 Marlow Ave.
San Antonio,TX 78299
www.klshelfoutfitters.example
klpo@klshelfoutfitter.example
(210) 555-0188
M-F: 9-6pm
Sat: 10-3pm

```html
<!DOCTYPE html>
<html lang="en">
<head>
<meta charset="utf-8">
<title>KL Shelf Outfitters – Business Card</title>
<link rel="stylesheet" href="https://fonts.googleapis.com/css2?family=Arimo:wght@400;700&display=swap">
<style>
  :root {
    --page: #e6e2dc;
    --card-black: #141414;
    --card-black-soft: #222222;
    --band-grey: #8e8e8e;
    --band-yellow: #e8c62a;
    --ink-dark: #1a1a1a;
    --ink-light: #f4f4f4;
    --photo-light: #f2f2f2;
    --photo-mid: #d9d6d2;
  }
  * { box-sizing: border-box; margin: 0; padding: 0; }
  html, body { width: 1200px; height: 892px; overflow: hidden; }
  body {
    background: var(--page);
    font-family: "Arimo", Arial, sans-serif;
    position: relative;
  }
  .card {
    position: absolute;
    top: 116px;
    width: 380px;
    height: 660px;
    background: linear-gradient(180deg, var(--card-black-soft) 0%, var(--card-black) 40%, var(--card-black) 100%);
    border-radius: 4px;
    overflow: hidden;
    box-shadow: 0 10px 28px rgba(0,0,0,.25);
  }
  .card--front { left: 170px; }
  .card--back { left: 650px; }

  .brand {
    position: absolute;
    display: flex;
    align-items: center;
    gap: 16px;
  }
  .brand__mark {
    width: 54px; height: 54px;
    background: var(--band-yellow);
    border-radius: 6px;
    flex: none;
  }
  .brand__name {
    color: var(--ink-light);
    font-weight: 700;
    font-size: 30px;
    line-height: 1.05;
    text-transform: uppercase;
    letter-spacing: 1px;
  }
  .card--front .brand { left: 40px; top: 110px; }
  .card--back .brand { left: 40px; top: 70px; }

  .band {
    position: absolute;
    left: 0; right: 0;
    display: flex;
    align-items: center;
    gap: 12px;
    padding: 0 22px;
    font-size: 21px;
    color: var(--ink-dark);
  }
  .band--grey { background: var(--band-grey); color: var(--ink-light); }
  .band--yellow { background: var(--band-yellow); }
  .band__icon { width: 20px; height: 20px; flex: none; }
  .band--address { align-items: flex-start; padding-top: 12px; line-height: 1.2; }

  .band--phone { top: 262px; height: 50px; }
  .band--web { top: 332px; height: 50px; }
  .band--email { top: 402px; height: 50px; }
  .band--address { top: 472px; height: 82px; }

  .product-strip {
    position: absolute;
    left: 0; right: 0;
    top: 214px; height: 196px;
    background: linear-gradient(90deg, var(--photo-light) 0%, var(--photo-mid) 55%, var(--photo-light) 100%);
    border-top: 5px solid var(--band-yellow);
    border-bottom: 5px solid var(--band-yellow);
  }
  .band--hours { top: 440px; height: 52px; justify-content: center; font-size: 20px; }
  .band--saturday { top: 514px; height: 54px; justify-content: center; font-size: 21px; }
</style>
</head>
<body>
  <section class="card card--front" aria-label="Business card front">
    <div class="brand">
      <span class="brand__mark"></span>
      <span class="brand__name">KL Shelf<br>Outfitters</span>
    </div>

    <div class="band band--grey band--phone">
      <svg class="band__icon" viewBox="0 0 20 20"><rect width="20" height="20" rx="3" fill="#f4f4f4"/><path d="M6 4l3 3-1.5 1.5a8 8 0 0 0 4 4L13 11l3 3-2 2C9 16 4 11 4 6z" fill="#8e8e8e"/></svg>
      <span>(210) 555-0188</span>
    </div>
    <div class="band band--yellow band--web">
      <svg class="band__icon" viewBox="0 0 20 20"><rect width="20" height="20" rx="3" fill="#1a1a1a"/><circle cx="10" cy="10" r="6" fill="none" stroke="#e8c62a" stroke-width="1.5"/><path d="M4 10h12M10 4c-3 3-3 9 0 12M10 4c3 3 3 9 0 12" fill="none" stroke="#e8c62a" stroke-width="1.2"/></svg>
      <span>www.klshelfoutfitters.example</span>
    </div>
    <div class="band band--grey band--email">
      <svg class="band__icon" viewBox="0 0 20 20"><rect width="20" height="20" rx="3" fill="#f4f4f4"/><rect x="4" y="6" width="12" height="8" fill="none" stroke="#8e8e8e" stroke-width="1.5"/><path d="M4 6l6 5 6-5" fill="none" stroke="#8e8e8e" stroke-width="1.5"/></svg>
      <span>klpo@klshelfoutfitter.example</span>
    </div>
    <div class="band band--yellow band--address">
      <svg class="band__icon" viewBox="0 0 20 20"><rect width="20" height="20" rx="3" fill="#1a1a1a"/><path d="M10 4a4 4 0 0 1 4 4c0 3-4 8-4 8s-4-5-4-8a4 4 0 0 1 4-4z" fill="#e8c62a"/><circle cx="10" cy="8" r="1.5" fill="#1a1a1a"/></svg>
      <span>4362 Marlow Ave. San Antonio<br>TX 78299</span>
    </div>
  </section>

  <section class="card card--back" aria-label="Business card back">
    <div class="brand">
      <span class="brand__mark"></span>
      <span class="brand__name">KL Shelf<br>Outfitters</span>
    </div>

    <div class="product-strip" role="img" aria-label="Product photos: clothing rack, glass display case, red wall shelving unit and dress form mannequin"></div>

    <div class="band band--grey band--hours">Mon day - Fri day :- 9.00 am - 6.00 pm</div>
    <div class="band band--yellow band--saturday">Satur day 10 am - 3.00 pm</div>
  </section>
</body>
</html>
```